Letterhead and Envelope for Mental Health Business

I need letterhead and envelope designs that will match my business cards. I am attaching a *.pds file of my business card so it can be matched.

Business

```html
<!DOCTYPE html>
<html lang="en">
<head>
<meta charset="utf-8">
<title>Alder Counseling Stationery</title>
<link href="https://fonts.googleapis.com/css2?family=Arimo:ital,wght@0,400;0,700;1,400&display=swap" rel="stylesheet">
<style>
  :root {
    --brand-blue: #2d5f93;
    --brand-green: #5a9a3a;
    --paper: #ffffff;
    --backdrop: #e9e7e3;
    --watermark: #f1f1f1;
    --window-edge: #d9d9d9;
  }
  * { margin: 0; padding: 0; box-sizing: border-box; }
  html, body {
    width: 1200px; height: 960px; overflow: hidden;
    background: var(--backdrop);
    font-family: "Arimo", Arial, sans-serif;
  }
  .stage { position: relative; width: 1200px; height: 960px; }

  .letterhead {
    position: absolute; left: 140px; top: 90px;
    width: 600px; height: 790px;
    background: var(--paper);
    box-shadow: 0 4px 14px rgba(0,0,0,.18);
    overflow: hidden;
  }
  .envelope {
    position: absolute; left: 450px; top: 355px;
    width: 730px; height: 345px;
    background: var(--paper);
    box-shadow: -4px 4px 16px rgba(0,0,0,.25);
    overflow: hidden;
  }

  .watermark {
    position: absolute; border-radius: 50%;
    background: var(--watermark);
  }
  .letterhead .watermark { width: 300px; height: 300px; left: 150px; top: 240px; }
  .envelope .watermark { width: 300px; height: 300px; left: 330px; top: -10px; }

  .brand { display: flex; align-items: center; gap: 10px; position: relative; }
  .brand-dot { border-radius: 50%; background: var(--brand-green); flex: none; }
  .brand-name {
    color: var(--brand-blue); font-weight: 700; line-height: 1;
    letter-spacing: .02em;
  }
  .person-name { color: var(--brand-blue); letter-spacing: .12em; position: relative; }
  .credentials { color: var(--brand-green); font-style: italic; letter-spacing: .14em; position: relative; }

  .letterhead-header {
    position: absolute; top: 50px; left: 0; width: 100%;
    display: flex; flex-direction: column; align-items: center;
  }
  .letterhead-header .brand-dot { width: 36px; height: 36px; }
  .letterhead-header .brand-name { font-size: 30px; }
  .letterhead-header .person-name { font-size: 22px; margin-top: 14px; }
  .letterhead-header .credentials { font-size: 11px; margin-top: 6px; }

  .envelope-header { position: absolute; left: 24px; top: 38px; }
  .envelope-header .brand-dot { width: 50px; height: 50px; }
  .envelope-header .brand-name { font-size: 38px; }
  .envelope-header .person-name { font-size: 30px; margin-top: 20px; }
  .envelope-header .credentials { font-size: 15px; margin-top: 8px; }

  .address-window {
    position: absolute; left: 465px; top: 90px;
    width: 260px; height: 140px;
    border: 1px solid var(--window-edge); border-radius: 8px;
    background: #fafafa;
  }

  .contact-band {
    position: absolute; left: 0; bottom: 0; width: 100%;
    background: var(--brand-blue); color: var(--paper);
    font-size: 10.5px; font-weight: 700; letter-spacing: .1em; line-height: 1.75;
  }
  .letterhead .contact-band { height: 92px; padding-top: 20px; text-align: center; font-size: 9.5px; }
  .envelope .contact-band { height: 86px; padding: 10px 22px; }
</style>
</head>
<body>
<main class="stage">
  <section class="letterhead" aria-label="Letterhead">
    <div class="watermark" aria-hidden="true"></div>
    <header class="letterhead-header">
      <div class="brand">
        <span class="brand-dot"></span>
        <span class="brand-name">Alder Counseling</span>
      </div>
      <div class="person-name">Martin Hale</div>
      <div class="credentials">LMHC, NCC, DCC</div>
    </header>
    <footer class="contact-band">
      <div>Elm Street 48, 2210 Portland, USA</div>
      <div>555/301-0142</div>
      <div>martinh@aldercounselingllc.com</div>
      <div>www.aldercounselingllc.com</div>
    </footer>
  </section>

  <section class="envelope" aria-label="Envelope">
    <div class="watermark" aria-hidden="true"></div>
    <header class="envelope-header">
      <div class="brand">
        <span class="brand-dot"></span>
        <span class="brand-name">Alder Counseling</span>
      </div>
      <div class="person-name">Martin Hale</div>
      <div class="credentials">LMHC, NCC, DCC</div>
    </header>
    <div class="address-window" aria-hidden="true"></div>
    <footer class="contact-band">
      <div>Elm Street 48, 2210 Portland, USA</div>
      <div>555/301-0142</div>
      <div>martinh@aldercounselingllc.com</div>
      <div>www.aldercounselingllc.com</div>
    </footer>
  </section>
</main>
</body>
</html>
```